Business Cards

I'm an contractor and consultant in IT Project management. I'd like a design for business cards.
In my work I mostly meet clients, peer project managers and technical staff. I usually exchange business cards at technical conventions or when networking.
I provide services that are:
- Updated, always with a fresh look on technology
- Solid and reliable
- Flexible schedule and always available
The current business card has been attached to provide information.
Target Market(s)
IT managers, IT project managers, consultants, recruitment staff. Age 30-45 years. College/University degree.
Industry/Entity Type
Contractor
Colors
Designer to choose colors to be used in the design.
Requirements
Must have
- Two sides, one side with personal information and the other side with company name.
Text in Norwegian, including Norwegian characters
Nice to have
- It should be possible for non-Norwegian speakers to read the contact details.

```html
<!DOCTYPE html>
<html lang="no">
<head>
<meta charset="utf-8">
<title>Eirik Sæland – visittkort</title>
<link rel="stylesheet" href="https://fonts.googleapis.com/css2?family=Josefin+Sans:wght@300;400&display=swap">
<style>
  :root {
    --backdrop: #8d8d8d;
    --card: #f1f1f1;
    --card-edge: #e4e4e4;
    --ink: #111111;
    --shadow: rgba(0, 0, 0, 0.28);
  }
  * { box-sizing: border-box; margin: 0; padding: 0; }
  html, body {
    width: 1200px;
    height: 1200px;
    overflow: hidden;
    background: var(--backdrop);
    font-family: "Josefin Sans", Arial, sans-serif;
    color: var(--ink);
  }
  .sheet {
    width: 1200px;
    height: 1200px;
    display: flex;
    flex-direction: column;
    align-items: center;
    justify-content: center;
    gap: 60px;
  }
  .card {
    position: relative;
    width: 900px;
    height: 510px;
    background: linear-gradient(135deg, #f7f7f7 0%, var(--card) 55%, var(--card-edge) 100%);
    box-shadow: 0 10px 30px var(--shadow);
  }
  /* Front: company side */
  .card--front {
    display: flex;
    flex-direction: column;
    align-items: center;
    justify-content: center;
    gap: 34px;
  }
  .brand-name {
    font-weight: 300;
    font-size: 64px;
    letter-spacing: 2px;
    text-transform: uppercase;
    line-height: 1;
  }
  .brand-role {
    font-weight: 300;
    font-size: 22px;
    letter-spacing: 5px;
    text-transform: uppercase;
  }
  /* Back: personal side */
  .card--back {
    display: flex;
    align-items: center;
  }
  .identity {
    width: 400px;
    padding-left: 70px;
    display: flex;
    flex-direction: column;
    gap: 18px;
  }
  .identity .brand-name { font-size: 38px; letter-spacing: 1px; }
  .company {
    font-weight: 300;
    font-size: 13px;
    letter-spacing: 3px;
    text-transform: uppercase;
  }
  .divider {
    width: 2px;
    height: 330px;
    flex: none;
  }
  .contact {
    list-style: none;
    padding-left: 50px;
    display: flex;
    flex-direction: column;
    gap: 26px;
    font-weight: 400;
    font-size: 20px;
    letter-spacing: 0.3px;
  }
  .contact .label { margin-right: 6px; }
</style>
</head>
<body>
  <main class="sheet">
    <section class="card card--front" aria-label="Forside">
      <h1 class="brand-name">Eirik Sæland</h1>
      <p class="brand-role">IT rådgiver</p>
    </section>

    <section class="card card--back" aria-label="Bakside">
      <div class="identity">
        <p class="brand-name">Eirik Sæland</p>
        <p class="company">Sæland Consulting</p>
      </div>
      <svg class="divider" viewBox="0 0 2 330" aria-hidden="true">
        <line x1="1" y1="0" x2="1" y2="330" stroke="#111111" stroke-width="2"/>
      </svg>
      <ul class="contact">
        <li><span class="label">M:</span>+47 90012345</li>
        <li><span class="label">E:</span>eirik@saelandconsulting.no</li>
        <li><span class="label">L:</span>http://www.saelandconsulting.no/profil</li>
        <li><span class="label">A:</span>Fjellveien 14, 0487 Oslo</li>
      </ul>
    </section>
  </main>
</body>
</html>
```